Web design for Money Service Business (uncoded)

We need a very basic website with 5-6 pages. Home page, Services, Transfer(How to use our service), About us, Contact us, FAQ
Our company name is Meridale Exchange. We are a company that deals with currency exchange and international money transfer. We do cash exchange and international money transfers to bank accounts all over the world. We offer highly competitive exchange rates so usually attract customers who transfer money over $10,000. Our niche is with larger sums of money, the design needs to be professional and communicate trust, security and stability.

```html
<!DOCTYPE html>
<html lang="en">
<head>
<meta charset="utf-8">
<title>Meridale Exchange – International Money Transfer</title>
<link rel="stylesheet" href="https://fonts.googleapis.com/css2?family=Jost:wght@400;500&family=Open+Sans:wght@400&family=Arimo:wght@400&display=swap">
<style>
  :root {
    --navy: #3b5a86;
    --navy-dark: #2f4b74;
    --nav-line: #6f88ab;
    --orange: #e9a247;
    --orange-deep: #de853a;
    --orange-light: #f2c17f;
    --white: #ffffff;
    --ink-blue: #3a5f95;
    --footer-ink: #3d5a8c;
    --panel-grey: #e6e9ee;
  }
  * { box-sizing: border-box; margin: 0; padding: 0; }
  html, body { width: 1200px; height: 879px; overflow: hidden; background: var(--white); }
  body { position: relative; font-family: "Open Sans", sans-serif; }

  .brand { position: absolute; left: 80px; top: 22px; display: flex; flex-direction: column; }
  .brand-name { display: flex; align-items: center; gap: 12px; font-family: "Jost", sans-serif; font-weight: 500; font-size: 54px; line-height: 58px; color: var(--navy); letter-spacing: -1px; }
  .brand-mark { width: 42px; height: 42px; border-radius: 50%; background: var(--navy); }
  .brand-tagline { font-family: "Jost", sans-serif; font-size: 22px; letter-spacing: 5.6px; color: var(--navy); margin-top: 6px; }

  .client-login { position: absolute; left: 930px; top: 0; width: 190px; height: 50px; background: var(--orange); border-radius: 0 0 6px 6px; color: var(--white); font-family: "Jost", sans-serif; font-size: 21px; display: flex; align-items: center; padding-left: 20px; }
  .client-login svg { margin-right: 42px; }
  .my-account { position: absolute; left: 1055px; top: 57px; font-family: "Arimo", sans-serif; font-size: 10px; color: var(--ink-blue); text-decoration: underline; }

  .main-nav { position: absolute; left: 80px; top: 127px; width: 807px; height: 37px; background: var(--navy); display: flex; }
  .main-nav a { flex: 1; color: var(--white); text-decoration: none; font-family: "Jost", sans-serif; font-size: 21px; display: flex; align-items: center; justify-content: center; border-right: 1px solid var(--nav-line); }
  .main-nav a:last-child { border-right: none; }

  .live-chat { position: absolute; left: 942px; top: 127px; width: 178px; height: 37px; background: linear-gradient(var(--orange-light), var(--orange)); border-radius: 0 6px 6px 0; color: var(--white); font-family: "Jost", sans-serif; font-size: 21px; display: flex; align-items: center; justify-content: flex-end; padding-right: 14px; }
  .chat-badge { position: absolute; left: 892px; top: 111px; width: 56px; height: 56px; border-radius: 50%; background: var(--white); border: 4px solid var(--orange); display: flex; align-items: center; justify-content: center; }

  .stage { position: absolute; left: 0; top: 172px; width: 1200px; height: 592px; background: var(--navy); }
  .hero-photo { position: absolute; left: 80px; top: 0; width: 842px; height: 365px; background: linear-gradient(135deg, #e9ecef 0%, #cfd8e2 45%, #6f9ccc 75%, #dde3ea 100%); }
  .register-btn { position: absolute; left: 552px; top: 23px; width: 335px; height: 46px; background: var(--navy); border: 3px solid #111; border-radius: 4px; color: var(--white); font-family: "Jost", sans-serif; font-size: 30px; display: flex; align-items: center; justify-content: center; }
  .globe-photo { position: absolute; left: 930px; top: 0; width: 190px; height: 289px; background: radial-gradient(circle at 45% 65%, #2f6a5a 0%, #1c3a4a 45%, #0c1622 100%); }

  .news-panel { position: absolute; left: 930px; top: 308px; width: 190px; height: 177px; background: var(--panel-grey); border-radius: 6px; border: 3px solid var(--white); }
  .news-tab { position: absolute; left: 36px; top: -3px; width: 115px; height: 28px; background: var(--orange-deep); color: var(--white); font-size: 15px; display: flex; align-items: center; justify-content: center; border-radius: 0 0 4px 4px; }
  .news-photo { position: absolute; left: 9px; top: 33px; width: 166px; height: 100px; background: linear-gradient(#ffffff, #dfe6ef 60%, #c9ced6); }
  .news-caption { position: absolute; left: 0; top: 136px; width: 100%; text-align: center; font-family: "Arimo", sans-serif; font-size: 9.5px; line-height: 12px; color: var(--ink-blue); text-decoration: underline; }

  .intro { position: absolute; left: 104px; top: 371px; width: 810px; color: var(--white); font-size: 19.6px; line-height: 20px; }

  .sections { position: absolute; left: 80px; top: 498px; width: 1040px; height: 44px; display: flex; }
  .sections a { flex: 1; background: var(--orange); color: var(--white); text-decoration: none; font-family: "Jost", sans-serif; font-size: 15px; letter-spacing: 0.5px; display: flex; align-items: center; justify-content: center; }
  .sections a.active { background: var(--orange-deep); }

  .social { position: absolute; left: 524px; top: 557px; display: flex; gap: 8px; }
  .social span { width: 24px; height: 24px; border-radius: 2px; }

  .stripe-band { position: absolute; left: 0; top: 768px; width: 1200px; height: 42px; background: linear-gradient(var(--orange-light), #f5cf99); }

  .site-footer { position: absolute; left: 0; top: 826px; width: 1200px; text-align: center; font-family: "Arimo", sans-serif; font-size: 15px; line-height: 19px; color: var(--footer-ink); }
  .site-footer a { color: var(--footer-ink); text-decoration: none; }
</style>
</head>
<body>
  <header>
    <div class="brand">
      <div class="brand-name"><span class="brand-mark"></span>MERIDALE EXCHANGE</div>
      <div class="brand-tagline">INTERNATIONAL MONEY TRANSFER</div>
    </div>
    <a class="client-login">
      <svg width="14" height="8" viewBox="0 0 14 8"><path d="M0 0h14L7 8z" fill="#fff"/></svg>
      Client Login
    </a>
    <a class="my-account">My Account</a>

    <nav class="main-nav">
      <a>Home</a><a>Services</a><a>Transfer</a><a>About Us</a><a>Contact Us</a><a>FAQ</a>
    </nav>
    <a class="live-chat">Live Chat</a>
    <span class="chat-badge">
      <svg width="28" height="24" viewBox="0 0 28 24"><ellipse cx="12" cy="9" rx="11" ry="8" fill="#e9a247"/><path d="M6 15l-3 7 8-5z" fill="#e9a247"/><ellipse cx="16" cy="12" rx="7" ry="5" fill="#fff"/><ellipse cx="16" cy="12" rx="5" ry="3.4" fill="#e9a247"/></svg>
    </span>
  </header>

  <main class="stage">
    <div class="hero-photo" role="img" aria-label="Business people reviewing financial bar charts at a desk"></div>
    <a class="register-btn">REGISTER NOW</a>
    <div class="globe-photo" role="img" aria-label="Earth at night with glowing global network lines"></div>

    <aside class="news-panel">
      <div class="news-tab">NEWS</div>
      <div class="news-photo" role="img" aria-label="Business team standing on a globe held in an open hand"></div>
      <p class="news-caption">Business team work worldwide<br>on a hand over</p>
    </aside>

    <p class="intro">We are a company that deals with currency exchange and international money transfer. We do cash exchange and international money transfers to bank accounts all over the world. We offer highly competitive exchange rates so usually attract customers who transfer money over $10,000. Our niche is with larger sums of money, the design needs to be professional and communicate trust, security and stability.</p>

    <nav class="sections">
      <a>FOREX</a><a class="active">COMMODITY</a><a>EDUCATION</a>
    </nav>

    <div class="social">
      <span style="background:#4a66a0"></span>
      <span style="background:#d6493b"></span>
      <span style="background:#1a77b5"></span>
      <span style="background:#c8232c;border-radius:50%"></span>
      <span style="background:#55acee"></span>
    </div>
  </main>

  <div class="stripe-band" role="img" aria-label="Diagonal orange stripe band"></div>

  <footer class="site-footer">
    <p>© Meridale Exchange 2013</p>
    <p><a>Privacy Statement</a> | <a>Risk Disclosure</a> | <a>Terms &amp; Conditions</a> | <a>Sitemap</a> | <a>Trading Platforms</a> | <a>Conflict Of Interest Policy</a></p>
  </footer>
</body>
</html>
```